RTV CRAFTED

building services
decks
pergola
renovation
extensions
general building

Target Market(s)

middle to upper class

Industry/Entity Type

building

Contact Information for Business Card

my details 0427839152 pkharlow47@mailvane.net BLD574926

Font styles to use
Serif

Colors
00AB8E
00BBA5
67D7C9
C6EFE9
E9F9F6

Requirements
Must have
• logo on the front and details on the back
Nice to have
• sharp and clean lines

```html
<!DOCTYPE html>
<html lang="en">
<head>
<meta charset="utf-8">
<title>RTV Crafted – Business Card</title>
<link href="https://fonts.googleapis.com/css2?family=Montserrat:wght@400;500;600;700&display=swap" rel="stylesheet">
<style>
  :root {
    --backdrop: #3b3b3b;
    --card-light: #ffffff;
    --card-dark: #231f20;
    --ink: #231f20;
    --ink-soft: #3a3a3a;
    --rule: #6b6b6b;
    --paper-ink: #ffffff;
  }
  * { margin: 0; padding: 0; box-sizing: border-box; }
  html, body {
    width: 1200px; height: 897px; overflow: hidden;
    background: var(--backdrop);
    font-family: "Montserrat", sans-serif;
  }
  .card {
    position: absolute; left: 329px; width: 543px; height: 310px;
  }
  .card-front { top: 108px; background: var(--card-light); color: var(--ink); }
  .card-back { top: 479px; background: var(--card-dark); }

  .brand-name {
    position: absolute; font-weight: 700; letter-spacing: 1px; white-space: nowrap;
  }
  .card-front .brand-name {
    right: 34px; top: 34px; font-size: 27px; color: var(--ink);
  }
  .card-back .brand-name {
    left: 0; right: 0; top: 128px; text-align: center;
    font-size: 44px; color: var(--paper-ink);
  }

  .edge-tab {
    position: absolute; left: 0; top: 134px; width: 8px; height: 32px; background: var(--ink);
  }
  .person-name {
    position: absolute; left: 32px; top: 131px; font-size: 18px; font-weight: 500; letter-spacing: 0.3px;
  }
  .person-role {
    position: absolute; left: 32px; top: 153px; font-size: 13px; color: var(--ink-soft); letter-spacing: 0.3px;
  }
  .divider {
    position: absolute; left: 32px; top: 179px; width: 318px; height: 1px; background: var(--rule);
  }
  .services-title {
    position: absolute; right: 35px; top: 170px; font-size: 14px; font-weight: 600;
  }
  .services-list {
    position: absolute; right: 35px; top: 192px; list-style: none; text-align: right;
  }
  .services-list li {
    font-size: 13.5px; line-height: 18px; color: var(--ink-soft);
    display: flex; justify-content: flex-end; align-items: center; gap: 7px;
  }
  .services-list li::after {
    content: ""; width: 9px; height: 9px; border-radius: 50%; background: var(--ink);
  }
  .licence {
    position: absolute; left: 32px; top: 219px; font-size: 13.5px; color: var(--ink-soft);
  }
  .contact {
    position: absolute; left: 32px; top: 245px; list-style: none;
  }
  .contact li {
    font-size: 13.5px; line-height: 18px; color: var(--ink-soft);
    display: flex; align-items: center; gap: 5px;
  }
  .contact svg { width: 10px; height: 10px; flex: none; }
</style>
</head>
<body>
  <section class="card card-front">
    <div class="brand-name">RTV CRAFTED</div>
    <div class="edge-tab"></div>
    <div class="person-name">DANIEL HARCOURT</div>
    <div class="person-role">DIRECTOR</div>
    <div class="divider"></div>
    <div class="services-title">BUILDING SERVICES</div>
    <ul class="services-list">
      <li>Decks</li>
      <li>Pergola</li>
      <li>Renovation</li>
      <li>Extensions</li>
      <li>General building</li>
    </ul>
    <div class="licence">BLD574926</div>
    <ul class="contact">
      <li>
        <svg viewBox="0 0 10 10" aria-hidden="true"><path d="M2.2 0.8 L3.6 2.6 L2.8 3.6 C3.3 4.9 4.6 6.3 6 6.9 L7 6.1 L8.9 7.5 L8 9.1 C4.4 8.9 1 5.3 0.8 1.8 Z" fill="none" stroke="#231f20" stroke-width="0.9"/></svg>
        0427839152
      </li>
      <li>
        <svg viewBox="0 0 10 10" aria-hidden="true"><rect x="0.6" y="2" width="8.8" height="6" fill="none" stroke="#231f20" stroke-width="0.9"/><path d="M0.8 2.3 L5 5.4 L9.2 2.3" fill="none" stroke="#231f20" stroke-width="0.9"/></svg>
        pkharlow47@mailvane.net
      </li>
    </ul>
  </section>

  <section class="card card-back">
    <div class="brand-name">RTV CRAFTED</div>
  </section>
</body>
</html>
```